Grafitti Inspired Underwear Brand Needs Website

Rex's Briefs needs a website concept for our upcoming ecommerce site. Rex’s Briefs is an underwear line targeting a male demographic between 16 and 25. The logo is in the attachments. The brand is a colorful, rebellious underwear brand targeting men who are all about getting noticed and having a good time. And especially about meeting women. We need a website concept than will transport the audience into a world of rebellion, color and fun. We are totally open to ideas, but our initial thought is its an urban, graffiti jungle. It should be a transportive web environment that will make the audience feel they are entering this other world. It could be a street setting or it could be an alleyway (googling grafitti alleyway gives some ideas) or something else.

One challenge will be to create this colorful setting against which the various navigation tabs and product pictures will stand out in such a way as to allow easy e-commerce. Maybe the setting could be a building or garage with windows that the tabs would be set against for visibility.

Here is something we really like, but we have no idea how to make the various navigation tabs visible against a background as colorful and varied as this.

http://tapestrynook.example/w/Zk7pR2m

The brand is based on colorful and edgy designs that may certainly be provocative and even sexist in some minds. Similar brands are Tornavelo and Sven Lakso (before the went unisex fitness.) Please visit those brand sites to get an idea of what the product will look like.

From an executional perspective, the primary navigation tabs are in the attached map.

Again, this is an ecommerce site so saleable product must be easily visible on the homepage and elsewhere. The basic structure should be pretty standard with Hero A’s, Hero B’s, product shots and promotion boxes all very visible, but what we need is a really cool environment concept.

Primary navigation tabs should be horizontal across the top of the site in a pretty standard fashion and are:

1. Dangerous Rex’s
2. Wild Rex’s
3. Plain Rex’s
4. All the Damn Rex’s
5. Design Rex’s
6. Rex’s Life
7. Rex’s Jokes
8. About Rex’s

Target Market(s)

Men 16-25

Number of Pages Required

1 page

Requirements
Must have
• Brand Logo.
Nice to have
• Fun use of the devil/heart logo

```html
<!DOCTYPE html>
<html lang="en">
<head>
<meta charset="utf-8">
<title>Rex's Briefs</title>
<link rel="stylesheet" href="https://fonts.googleapis.com/css2?family=Lobster&family=Open+Sans:wght@400;600;700&display=swap">
<style>
  :root {
    --purple: #5b2a86;
    --purple-dark: #4a1f70;
    --green: #7ac142;
    --green-dark: #5fa12d;
    --ink: #333333;
    --muted: #8a8a8a;
    --line: #e4e4e4;
    --white: #ffffff;
    --panel: #f3f3f3;
    --dark: #2b2b2b;
  }
  * { box-sizing: border-box; margin: 0; padding: 0; }
  html, body { width: 698px; height: 1200px; overflow: hidden; }
  body { font-family: "Open Sans", Arial, sans-serif; color: var(--ink); background: var(--white); font-size: 8px; }

  .site-header { height: 62px; display: flex; align-items: center; justify-content: space-between; padding: 0 62px; background: var(--white); }
  .brand { display: flex; align-items: center; gap: 6px; font-family: "Lobster", cursive; font-size: 20px; color: var(--purple); }
  .brand-dot { width: 14px; height: 14px; border-radius: 50%; background: var(--green); }
  .header-tools { display: flex; gap: 6px; }
  .tool { width: 18px; height: 18px; border-radius: 50%; background: #e9e9e9; display: flex; align-items: center; justify-content: center; }

  .main-nav { height: 32px; background: var(--purple); display: flex; align-items: stretch; padding: 0 62px; }
  .main-nav a { color: var(--white); text-decoration: none; font-size: 6.5px; font-weight: 700; text-transform: uppercase; display: flex; align-items: center; padding: 0 9px; letter-spacing: .2px; }
  .main-nav a.active { background: var(--green); }

  .hero { height: 246px; position: relative; background: linear-gradient(135deg, #2a2a3a 0%, #45304f 35%, #2d3d4a 65%, #1e1e26 100%); }
  .hero-product { position: absolute; left: 190px; top: 30px; width: 130px; height: 110px; border-radius: 6px; background: linear-gradient(135deg, #3d7fd1, #e6d93a 50%, #3d7fd1); }
  .hero-copy { position: absolute; left: 375px; top: 70px; width: 230px; color: var(--white); }
  .hero-title { font-family: "Lobster", cursive; font-size: 38px; font-weight: 400; }
  .hero-text { font-size: 6px; line-height: 1.6; margin: 4px 0 12px; color: #e6e6e6; }

  .btn { display: inline-flex; align-items: center; gap: 4px; background: var(--green); color: var(--white); font-size: 6px; font-weight: 700; text-transform: uppercase; padding: 6px 12px; border: 0; }

  .backdrop { position: relative; height: 614px; background: linear-gradient(160deg, #e7e53a 0%, #c9d93a 20%, #d63a3a 45%, #f0e34a 60%, #c22e2e 80%, #e6df38 100%); }
  .content { position: absolute; left: 78px; top: 8px; width: 542px; background: var(--white); }
  .intro { text-align: center; padding: 22px 40px 20px; border-bottom: 1px solid var(--line); }
  .section-title { font-family: "Lobster", cursive; font-size: 22px; font-weight: 400; }
  .intro .section-title { color: var(--green); }
  .intro p { font-size: 6px; line-height: 1.7; color: var(--muted); margin: 8px 0 10px; }

  .arrivals { padding: 18px 18px 24px; text-align: center; }
  .arrivals .section-title { color: var(--purple); margin-bottom: 16px; }
  .product-grid { display: flex; justify-content: space-between; }
  .product-card { width: 150px; background: var(--panel); padding: 10px 10px 12px; }
  .product-image { height: 100px; border-radius: 2px; }
  .img-a { background: linear-gradient(135deg, #7a1f55, #d2453a 50%, #f0b23a); }
  .img-b { background: linear-gradient(135deg, #3a7fd1, #c6397c 50%, #3d3d8f); }
  .img-c { background: linear-gradient(135deg, #1c1c1c, #3a3a3a 60%, #7ac142); }
  .product-name { font-size: 5.5px; text-transform: uppercase; color: var(--muted); margin: 10px 0 5px; }
  .price { font-size: 12px; color: var(--ink); margin-bottom: 8px; }

  .promos { position: absolute; left: 78px; top: 442px; width: 542px; display: flex; justify-content: space-between; }
  .promo { width: 260px; height: 98px; color: var(--white); text-align: center; padding-top: 22px; }
  .promo-offer { background: var(--purple); }
  .promo-weekend { background: var(--dark); }
  .promo h3 { font-size: 15px; font-weight: 600; text-transform: uppercase; letter-spacing: .5px; }
  .promo p { font-size: 5.5px; line-height: 1.6; margin: 6px 30px 0; color: #ddd; }

  .site-footer { height: 210px; padding: 24px 62px 0; display: grid; grid-template-columns: repeat(4, 1fr); gap: 14px; }
  .site-footer h4 { font-size: 8px; text-transform: uppercase; font-weight: 700; margin-bottom: 10px; }
  .site-footer li { list-style: none; font-size: 5.5px; color: var(--muted); margin-bottom: 7px; display: flex; align-items: center; gap: 5px; }
  .socials { display: flex; gap: 4px; margin-top: 6px; }
  .social { width: 12px; height: 12px; background: #cfcfcf; }

  .bottom-bar { border-top: 1px solid var(--line); height: 40px; display: flex; align-items: center; justify-content: space-between; padding: 0 62px; font-size: 5.5px; color: var(--muted); }
  .payments { display: flex; gap: 4px; }
  .pay { width: 14px; height: 9px; background: #d9d9d9; }
</style>
</head>
<body>
  <header class="site-header">
    <div class="brand"><span class="brand-dot"></span>Rex's Briefs</div>
    <div class="header-tools">
      <span class="tool"><svg width="8" height="8" viewBox="0 0 10 10"><circle cx="4" cy="4" r="3" fill="none" stroke="#555" stroke-width="1.4"/><line x1="6.3" y1="6.3" x2="9" y2="9" stroke="#555" stroke-width="1.4"/></svg></span>
      <span class="tool"><svg width="8" height="8" viewBox="0 0 10 10"><circle cx="5" cy="3" r="2.2" fill="#555"/><path d="M1 10c0-3 2-4.5 4-4.5s4 1.5 4 4.5z" fill="#555"/></svg></span>
      <span class="tool"><svg width="8" height="8" viewBox="0 0 10 10"><path d="M1 1h2l1.2 5h4.3L10 2.5H3.5" fill="none" stroke="#555" stroke-width="1.2"/><circle cx="4.5" cy="8.5" r="1" fill="#555"/><circle cx="8" cy="8.5" r="1" fill="#555"/></svg></span>
    </div>
  </header>

  <nav class="main-nav">
    <a class="active" href="#">Home</a>
    <a href="#">Dangerous Rex’s</a>
    <a href="#">Wild Rex’s</a>
    <a href="#">Plain Rex’s</a>
    <a href="#">All the Damn Rex’s</a>
    <a href="#">Design Rex’s</a>
    <a href="#">Rex’s Life</a>
    <a href="#">Rex’s Jokes</a>
    <a href="#">About Rex’s</a>
  </nav>

  <section class="hero" role="img" aria-label="Graffiti-covered alley wall behind a featured pair of patterned boxer briefs">
    <div class="hero-product" role="img" aria-label="Blue and yellow patterned boxer briefs"></div>
    <div class="hero-copy">
      <h1 class="hero-title">Design Rex’s</h1>
      <p class="hero-text">Bold prints made for the street. Loud colours, sharp cuts and a fit that keeps up with every night out you have planned.</p>
      <span class="btn">&#9656; Buy Now</span>
    </div>
  </section>

  <section class="backdrop" role="img" aria-label="Bright yellow and red graffiti collage backdrop">
    <div class="content">
      <div class="intro">
        <h2 class="section-title">Rex's Briefs</h2>
        <p>Underwear for guys who like to be seen. Every pair is built from soft stretch cotton with prints pulled straight off the city walls. Mix, match and wear them loud, because plain was never the plan and nobody remembers the quiet one at the party anyway.</p>
        <span class="btn">&#9656; Shop Now</span>
      </div>
      <div class="arrivals">
        <h2 class="section-title">New Arrivals</h2>
        <div class="product-grid">
          <article class="product-card">
            <div class="product-image img-a" role="img" aria-label="Red and orange printed boxer briefs"></div>
            <p class="product-name">Street blaze boxer brief</p>
            <p class="price">$ 27.50</p>
            <span class="btn">&#9656; Buy Now</span>
          </article>
          <article class="product-card">
            <div class="product-image img-b" role="img" aria-label="Blue and pink printed boxer briefs"></div>
            <p class="product-name">Neon alley boxer brief</p>
            <p class="price">$ 27.50</p>
            <span class="btn">&#9656; Buy Now</span>
          </article>
          <article class="product-card">
            <div class="product-image img-c" role="img" aria-label="Black boxer briefs with green waistband"></div>
            <p class="product-name">Night shift boxer brief</p>
            <p class="price">$ 27.50</p>
            <span class="btn">&#9656; Buy Now</span>
          </article>
        </div>
      </div>
    </div>

    <div class="promos">
      <div class="promo promo-offer">
        <h3>15% Offer</h3>
        <p>Take fifteen off your first order of any three pairs. Limited time only, grab yours today.</p>
      </div>
      <div class="promo promo-weekend">
        <h3>Week End Discount</h3>
        <p>Every Saturday and Sunday the whole range drops in price. Stock up before Monday hits.</p>
      </div>
    </div>
  </section>

  <footer class="site-footer">
    <div>
      <h4>Contact</h4>
      <ul>
        <li><svg width="7" height="7" viewBox="0 0 10 10"><path d="M5 0a3.5 3.5 0 0 0-3.5 3.5C1.5 6 5 10 5 10s3.5-4 3.5-6.5A3.5 3.5 0 0 0 5 0z" fill="#7ac142"/></svg>1955 Harlow Street, Suite 12</li>
        <li><svg width="7" height="7" viewBox="0 0 10 10"><path d="M2 0l2 2.5-1.2 1.5a6 6 0 0 0 3.2 3.2L7.5 6 10 8l-1.5 2C4 10 0 6 0 1.5z" fill="#7ac142"/></svg>(555) 014-2290</li>
      </ul>
      <div class="socials"><span class="social"></span><span class="social"></span><span class="social"></span><span class="social"></span></div>
    </div>
    <div>
      <h4>Products</h4>
      <ul><li>Boxer briefs collection</li><li>Printed trunks range</li><li>Plain cotton basics</li><li>Limited graffiti series</li><li>Gift packs and bundles</li></ul>
    </div>
    <div>
      <h4>Navigate</h4>
      <ul><li>Today Offer</li><li>About</li><li>Contact</li><li>Blog</li></ul>
    </div>
    <div>
      <h4>Support</h4>
      <ul><li>Sign In</li><li>Wishlist</li><li>Returns</li><li>FAQ</li><li>Sitemap</li></ul>
    </div>
  </footer>

  <div class="bottom-bar">
    <span>© 2016 Rex's Briefs. All Rights Reserved.</span>
    <div class="payments"><span class="pay"></span><span class="pay"></span><span class="pay"></span><span class="pay"></span></div>
  </div>
</body>
</html>
```